Web Design Project

Looking for an eye catching banner page to be used on the website and LinkedIn. We are an Executive Recruiting and HR Consulting service firm with a modern edge. We want to demonstrate through our brand that we are using the latest recruiting trends to find talent and that we are easy to work with- innovative and simple.We typically recruit for Engineers, IT professionals, Accounting and Operation Managers. Our website is www.harborlinetalent.com and it needs a fresh clean look. We love our logo but might want to use the "8" to show the 2 sides of our business or maybe to use the infinity concept or continuous improvement. We like the Green and white colors with accents in gray.

Target Market(s)

Small to mid-sized Business Managers seeking innovation

Industry/Entity Type

Business

Requirements
Must have
• Use of the 8
Long picture on top to be used on LinkedIn and the website top
Clean Simple look- modern font like century gothic
Nice to have
• Smiling face(s)
Layered image of 8 or of photo stock faces
Maybe a modern office so they feel that they walked in to meet us (fyi our office has white chandeliers and green walls that match our logo)
Should not have
• Busy or cluttered feel

```html
<!DOCTYPE html>
<html lang="en">
<head>
<meta charset="utf-8">
<title>Harborline Talent</title>
<link rel="stylesheet" href="https://fonts.googleapis.com/css2?family=Questrial&family=Arimo:wght@400;700&display=swap">
<style>
:root{
  --green:#a6b80a;
  --green-dark:#95a600;
  --slate:#383d46;
  --slate-deep:#30343c;
  --gray-btn:#5b6370;
  --orange:#e07a22;
  --text:#8a8a8a;
  --text-dark:#222;
  --rule:#dcdcdc;
  --nav-text:#e4e4e4;
  --white:#fff;
}
*{margin:0;padding:0;box-sizing:border-box}
html,body{width:1052px;height:1200px;overflow:hidden;background:var(--white)}
body{font-family:"Arimo",Arial,sans-serif;color:var(--text)}
.page{position:relative;width:1052px;height:1200px;overflow:hidden;border-top:2px solid var(--green)}

/* header */
.site-header{position:absolute;top:0;left:0;width:100%;height:63px}
.brand{position:absolute;left:162px;top:17px;display:flex;align-items:center;gap:8px;font-family:"Questrial",sans-serif;font-size:28px;letter-spacing:1px;color:var(--green)}
.brand-dot{width:12px;height:12px;border-radius:50%;background:var(--green)}
.audience{position:absolute;top:30px;left:700px;display:flex;gap:3px}
.audience a{display:block;width:92px;height:21px;line-height:21px;text-align:center;font-family:"Questrial",sans-serif;font-size:11px;color:var(--white);text-decoration:none}
.audience .candidates{background:var(--gray-btn)}
.audience .clients{background:var(--green)}

/* navigation */
.main-nav{position:absolute;top:63px;left:0;width:100%;height:37px;background:var(--slate)}
.main-nav ul{list-style:none;position:absolute;left:163px;width:724px;height:37px;display:flex;justify-content:space-between;align-items:center}
.main-nav li{font-size:10.5px;color:var(--nav-text)}
.main-nav li.sep{color:#6b707a;font-size:14px}
.main-nav li.active{color:var(--green)}

/* hero */
.hero{position:absolute;top:100px;left:0;width:100%;height:344px;
  background:
    radial-gradient(ellipse 330px 120px at 640px 330px,rgba(140,175,45,.55),rgba(140,175,45,0)),
    radial-gradient(ellipse 160px 110px at 1000px 300px,rgba(140,175,45,.35),rgba(140,175,45,0)),
    linear-gradient(100deg,#dfe1dd 0%,#c9ccc6 25%,#8d8b84 40%,#5e5b55 55%,#9a988f 72%,#d3d6d1 100%)}
.hero-tagline{position:absolute;left:161px;top:141px;width:459px;height:43px;background:rgba(70,72,74,.55);color:var(--white);font-family:"Questrial",sans-serif;font-weight:400;font-size:30px;line-height:43px;padding-left:18px}

/* services */
.services{position:absolute;top:480px;left:163px;width:724px;height:190px}
.service{position:absolute;top:0;width:220px;text-align:center}
.service .badge{display:block;margin:0 auto}
.service h2{margin-top:15px;font-family:"Questrial",sans-serif;font-weight:400;font-size:12px;color:var(--green);letter-spacing:.2px}
.service p{margin-top:12px;font-size:8.6px;line-height:12.7px;letter-spacing:.2px}
.flow-arrow{position:absolute;top:36px}
.services-curve{position:absolute;top:675px;left:163px}

/* expertise + testimonials */
.expertise{position:absolute;top:736px;left:163px;width:303px}
.section-title{font-family:"Questrial",sans-serif;font-weight:400;font-size:12px;color:var(--green);letter-spacing:.2px}
.expertise ul{list-style:none;margin-top:19px}
.expertise li{position:relative;height:17px;line-height:17px;padding-left:19px;font-size:8.6px;letter-spacing:.7px;text-transform:uppercase;border-bottom:1px dotted var(--rule)}
.expertise li:last-child{border-bottom:0}
.expertise li svg{position:absolute;left:0;top:5px}
.column-rule{position:absolute;top:738px;left:525px;height:186px;border-left:1px dotted var(--rule)}
.testimonials{position:absolute;top:736px;left:560px;width:327px}
.testimonials blockquote{margin-top:8px;font-size:8.6px;line-height:12.7px;letter-spacing:.2px}
.testimonials blockquote:first-of-type{margin-top:19px}
.testimonials cite{display:block;font-style:normal;font-size:8.6px;color:var(--text-dark);margin-top:2px;padding-left:1px}

/* footer */
.site-footer{position:absolute;top:957px;left:0;width:100%;height:176px;background:var(--slate)}
.footer-col{position:absolute;top:24px}
.footer-col h3{font-family:"Questrial",sans-serif;font-weight:400;font-size:12px;color:var(--white);letter-spacing:.3px}
.useful{left:163px}
.useful a{display:flex;justify-content:space-between;align-items:center;width:118px;height:18px;padding:0 8px;margin-bottom:7px;font-size:9px;color:var(--white);text-decoration:none}
.useful .links{margin-top:14px}
.btn-find{background:var(--orange)}
.btn-ats{background:var(--green)}
.btn-apply{background:var(--gray-btn)}
.quick{left:458px}
.quick ul,.contact ul{list-style:none;margin-top:13px}
.quick li{height:17px;line-height:17px;font-size:8.6px;color:#b9bcc2;letter-spacing:.4px;padding-left:13px;position:relative}
.quick li svg{position:absolute;left:0;top:6px}
.contact{left:731px}
.contact li{position:relative;height:17px;line-height:17px;font-size:8.6px;color:#b9bcc2;letter-spacing:.4px;padding-left:22px}
.contact li.name{color:var(--green)}
.contact li svg{position:absolute;left:0;top:3px}
.footer-rule{position:absolute;top:45px;height:108px;border-left:1px dotted #5b606a}

.legal{position:absolute;top:1133px;left:0;width:100%;height:67px;background:var(--slate-deep);border-bottom:3px solid var(--green)}
.legal p{position:absolute;left:163px;font-size:8.6px;color:#b9bcc2;letter-spacing:.3px}
.legal .mail{top:20px}
.legal .copy{top:36px}
.legal .copy span{color:var(--green)}
.social{position:absolute;left:734px;top:18px;display:flex;gap:2px;list-style:none}
.social li{width:24px;height:24px;border-radius:50%;background:#6e737b}
.social li.mailto{display:flex;align-items:center;justify-content:center}
</style>
</head>
<body>
<div class="page">

  <header class="site-header">
    <div class="brand">HARBORLINE<span class="brand-dot"></span></div>
    <nav class="audience">
      <a class="candidates" href="#">CANDIDATES</a>
      <a class="clients" href="#">CLIENTS</a>
    </nav>
  </header>

  <nav class="main-nav">
    <ul>
      <li class="active">Home</li><li class="sep">/</li>
      <li>About Us</li><li class="sep">/</li>
      <li>Recruiting Services</li><li class="sep">/</li>
      <li>HR Consulting Services</li><li class="sep">/</li>
      <li>Testimonials</li><li class="sep">/</li>
      <li>Job Openings</li><li class="sep">/</li>
      <li>Job Application</li><li class="sep">/</li>
      <li>Contact Us</li>
    </ul>
  </nav>

  <section class="hero" role="img" aria-label="Photo of a smiling recruiting team meeting around a white table in a bright modern office with green chairs">
    <h1 class="hero-tagline">Where strategy meets recruiting</h1>
  </section>

  <section class="services">
    <article class="service" style="left:0">
      <svg class="badge" width="72" height="72" viewBox="0 0 72 72">
        <circle cx="36" cy="36" r="35" fill="none" stroke="var(--green)" stroke-width="1.5"/>
        <circle cx="36" cy="36" r="31" fill="var(--green)"/>
        <circle cx="38" cy="26" r="4" fill="#fff"/>
        <path d="M26 40 L36 32 L44 36 L50 32" stroke="#fff" stroke-width="3" fill="none" stroke-linecap="round"/>
        <path d="M22 44 Q36 38 50 44" stroke="#fff" stroke-width="2" fill="none"/>
      </svg>
      <h2>RECRUITING</h2>
      <p>Harborline combines strategy and action to find high-impact hires in the areas of Engineering, IT/Technology, Operations, Executive Leadership, Accounting and Administration. We bring creative solutions to complex searches where other search firms have been unsuccessful.</p>
    </article>
    <svg class="flow-arrow" style="left:183px" width="40" height="8" viewBox="0 0 40 8"><path d="M0 4 H34" stroke="#ccc" stroke-dasharray="3 2"/><path d="M32 1 L37 4 L32 7" stroke="#ccc" fill="none"/></svg>
    <svg class="flow-arrow" style="left:268px" width="36" height="8" viewBox="0 0 36 8"><path d="M0 4 H36" stroke="#ddd" stroke-dasharray="3 2"/></svg>

    <article class="service" style="left:253px">
      <svg class="badge" width="72" height="72" viewBox="0 0 72 72">
        <circle cx="36" cy="36" r="35" fill="none" stroke="var(--green)" stroke-width="1.5"/>
        <circle cx="36" cy="36" r="31" fill="var(--green)"/>
        <path d="M20 32 L28 28 L36 32 L44 28 L52 32 L46 40 L38 44 L30 42 L24 38 Z" fill="none" stroke="#fff" stroke-width="2.5" stroke-linejoin="round"/>
        <path d="M30 36 L38 40 M33 33 L41 37" stroke="#fff" stroke-width="2"/>
      </svg>
      <h2>HUMAN RESOURCE CONSULTING</h2>
      <p>Our PHR/SPHR certified professional HR consultants partner with you to co-create sound HR processes and solutions to people challenges. Our solutions are always keeping in mind the most important asset of any organization…<br>it's employees!</p>
    </article>
    <svg class="flow-arrow" style="left:437px" width="40" height="8" viewBox="0 0 40 8"><path d="M0 4 H34" stroke="#ccc" stroke-dasharray="3 2"/><path d="M32 1 L37 4 L32 7" stroke="#ccc" fill="none"/></svg>
    <svg class="flow-arrow" style="left:523px" width="36" height="8" viewBox="0 0 36 8"><path d="M0 4 H36" stroke="#ddd" stroke-dasharray="3 2"/></svg>

    <article class="service" style="left:506px">
      <svg class="badge" width="72" height="72" viewBox="0 0 72 72">
        <circle cx="36" cy="36" r="35" fill="none" stroke="var(--green)" stroke-width="1.5"/>
        <circle cx="36" cy="36" r="31" fill="var(--green)"/>
        <rect x="25" y="25" width="10" height="10" fill="#fff"/>
        <rect x="37" y="25" width="10" height="10" fill="#fff"/>
        <rect x="25" y="37" width="10" height="10" fill="#fff"/>
        <rect x="39" y="39" width="10" height="10" fill="#fff"/>
        <circle cx="36" cy="30" r="2.5" fill="#fff"/>
        <circle cx="30" cy="36" r="2.5" fill="#fff"/>
      </svg>
      <h2>RECRUITING TURNKEY CONSULTING</h2>
      <p>Our scalable recruiting solutions provide you with an on-demand recruiting department at your fingertips for 1 to multiple hires. Our highly experienced team creates solutions are tailored to your needs from tapping into new candidate pools, screening resumes, interviewing, staff interview training,</p>
    </article>
  </section>

  <svg class="services-curve" width="724" height="50" viewBox="0 0 724 50" aria-hidden="true">
    <path d="M0 2 Q2 26 26 26 H332 Q354 26 362 48 Q370 26 392 26 H698 Q722 26 724 2" fill="none" stroke="#e6e6e6" stroke-width="1.2"/>
  </svg>

  <section class="expertise">
    <h2 class="section-title">RECRUITING AREAS OF EXPERTISE</h2>
    <ul>
      <li><svg width="6" height="8" viewBox="0 0 6 8"><path d="M1 0 L5 4 L1 8" stroke="#bbb" fill="none"/></svg>Administrative</li>
      <li><svg width="6" height="8" viewBox="0 0 6 8"><path d="M1 0 L5 4 L1 8" stroke="#bbb" fill="none"/></svg>Accounting</li>
      <li><svg width="6" height="8" viewBox="0 0 6 8"><path d="M1 0 L5 4 L1 8" stroke="#bbb" fill="none"/></svg>Engineering</li>
      <li><svg width="6" height="8" viewBox="0 0 6 8"><path d="M1 0 L5 4 L1 8" stroke="#bbb" fill="none"/></svg>Operations</li>
      <li><svg width="6" height="8" viewBox="0 0 6 8"><path d="M1 0 L5 4 L1 8" stroke="#bbb" fill="none"/></svg>Marketing</li>
      <li><svg width="6" height="8" viewBox="0 0 6 8"><path d="M1 0 L5 4 L1 8" stroke="#bbb" fill="none"/></svg>Sales</li>
      <li><svg width="6" height="8" viewBox="0 0 6 8"><path d="M1 0 L5 4 L1 8" stroke="#bbb" fill="none"/></svg>Human Resources</li>
      <li><svg width="6" height="8" viewBox="0 0 6 8"><path d="M1 0 L5 4 L1 8" stroke="#bbb" fill="none"/></svg>Technology</li>
      <li><svg width="6" height="8" viewBox="0 0 6 8"><path d="M1 0 L5 4 L1 8" stroke="#bbb" fill="none"/></svg>Medical</li>
    </ul>
  </section>

  <div class="column-rule"></div>

  <section class="testimonials">
    <h2 class="section-title">TESTIMONIALS</h2>
    <blockquote>"Harborline has been very attentive to the needs of our Corporation. From providing administrative to technical candidates, they operate in a professional manner and will go above and beyond to achieve exceptional results."<cite>Aerospace Contract Company</cite></blockquote>
    <blockquote>"Harborline delivered a depth of experience that we had never encountered in a recruiting agency, including a detailed understanding of our business needs and innovative solutions to help us achieve our goals."<cite>Technical Writing Firm</cite></blockquote>
    <blockquote>"What differentiates Harborline from other HR service firms is their desire to find the right HR solutions for your unique company culture."<cite>Architecture Firm</cite></blockquote>
  </section>

  <footer class="site-footer">
    <div class="footer-col useful">
      <h3>USEFULL LINKS</h3>
      <div class="links">
        <a class="btn-find" href="#">Find Job<span>›</span></a>
        <a class="btn-ats" href="#">Welcom to ATS<span>›</span></a>
        <a class="btn-apply" href="#">Apply Now<span>›</span></a>
      </div>
    </div>
    <div class="footer-rule" style="left:355px"></div>
    <div class="footer-col quick">
      <h3>QUICK LINKS</h3>
      <ul>
        <li><svg width="4" height="6" viewBox="0 0 4 6"><path d="M0 0 L4 3 L0 6Z" fill="var(--green)"/></svg>Home</li>
        <li><svg width="4" height="6" viewBox="0 0 4 6"><path d="M0 0 L4 3 L0 6Z" fill="var(--green)"/></svg>Recruiting Services</li>
        <li><svg width="4" height="6" viewBox="0 0 4 6"><path d="M0 0 L4 3 L0 6Z" fill="var(--green)"/></svg>HR Consulting Services</li>
        <li><svg width="4" height="6" viewBox="0 0 4 6"><path d="M0 0 L4 3 L0 6Z" fill="var(--green)"/></svg>Testimonials</li>
        <li><svg width="4" height="6" viewBox="0 0 4 6"><path d="M0 0 L4 3 L0 6Z" fill="var(--green)"/></svg>Job Openings</li>
        <li><svg width="4" height="6" viewBox="0 0 4 6"><path d="M0 0 L4 3 L0 6Z" fill="var(--green)"/></svg>Job Application</li>
        <li><svg width="4" height="6" viewBox="0 0 4 6"><path d="M0 0 L4 3 L0 6Z" fill="var(--green)"/></svg>Contact Us</li>
      </ul>
    </div>
    <div class="footer-rule" style="left:670px"></div>
    <div class="footer-col contact">
      <h3>CONTACT US</h3>
      <ul>
        <li class="name">Harborline Talent</li>
        <li><svg width="10" height="14" viewBox="0 0 10 14"><path d="M5 0 A5 5 0 0 1 10 5 C10 9 5 14 5 14 C5 14 0 9 0 5 A5 5 0 0 1 5 0Z" fill="var(--green)"/><circle cx="5" cy="5" r="2" fill="var(--slate)"/></svg>4180 Bayfront Commons Dr</li>
        <li>Suite 210 Port Lavell TX 77519</li>
        <li><svg width="12" height="10" viewBox="0 0 12 10"><path d="M0 3 Q6 -1 12 3 L10 5 L8 3 H4 L2 5Z M2 6 H10 V10 H2Z" fill="var(--green)"/></svg>555.214.0371</li>
        <li><svg width="8" height="12" viewBox="0 0 8 12"><rect x="0.5" y="0.5" width="7" height="11" rx="1" fill="none" stroke="var(--green)"/><rect x="2" y="2" width="4" height="6" fill="var(--green)"/></svg>555.388.1042</li>
        <li><svg width="12" height="10" viewBox="0 0 12 10"><rect x="0" y="3" width="12" height="7" fill="var(--green)"/><rect x="3" y="0" width="6" height="3" fill="var(--green)"/></svg>555.602.9157</li>
        <li><svg width="12" height="9" viewBox="0 0 12 9"><rect width="12" height="9" fill="var(--green)"/><path d="M0 0 L6 5 L12 0" stroke="var(--slate)" fill="none"/></svg>www.harborlinetalent.com</li>
      </ul>
    </div>
  </footer>

  <div class="legal">
    <p class="mail">info@harborlinetalent.com</p>
    <p class="copy">Copyright © 2013 <span>HARBORLINE</span></p>
    <ul class="social" aria-label="Social profiles">
      <li></li><li></li><li></li><li></li><li></li>
      <li class="mailto"><svg width="12" height="9" viewBox="0 0 12 9"><rect width="12" height="9" fill="#fff"/><path d="M0 0 L6 5 L12 0" stroke="#6e737b" fill="none"/></svg></li>
    </ul>
  </div>

</div>
</body>
</html>
```